Flyer für Therapie- und Gesundheitsdienstleister
Zielgruppe
Therapie- und Gesundheitsdienstleister im Bereich Physiotherapie, Podologie, Prävention und betriebliche Gesundheitsförderung. Für dieses Projekt möchten wir einen Flyer erstellen lassen für die Bewerbung der betrieblichen Gesundheitsförderungen in bzw. für Firmen
Aufgabenstellung
Klare Strukturen, nicht verspielt, DINA4 oder DINA5; leicht medizinischer Touch, evntuell Stockfotos integrieren, edel und hochwertiges Design

```html
<!DOCTYPE html>
<html lang="de">
<head>
<meta charset="utf-8">
<title>Betriebliche Gesundheitsförderung – Flyer</title>
<link rel="stylesheet" href="https://fonts.googleapis.com/css2?family=Mulish:wght@400;600;700;800&display=swap">
<style>
  :root {
    --orange: #ef8519;
    --ink: #3b3b3d;
    --ink-soft: #5a5a5c;
    --panel: #efefef;
    --band: #d8d8d8;
    --footer: #59595b;
    --paper: #ffffff;
    --stage: #ffffff;
  }
  * { box-sizing: border-box; margin: 0; padding: 0; }
  html, body { width: 1200px; height: 806px; overflow: hidden; background: var(--stage); }
  body { font-family: "Mulish", sans-serif; color: var(--ink); position: relative; }

  .page {
    position: absolute; top: 39px; width: 513px; height: 726px;
    background: var(--paper); overflow: hidden;
    box-shadow: 0 2px 8px rgba(0,0,0,.18);
  }
  .page--front { left: 47px; }
  .page--back { left: 639px; }

  .hero { position: absolute; left: 0; top: 0; }

  .badge {
    position: absolute; border-radius: 50%; background: var(--orange);
    color: #fff; font-weight: 800; text-align: center;
    display: flex; align-items: center; justify-content: center;
    box-shadow: 0 3px 6px rgba(0,0,0,.25);
  }
  .badge span { display: block; transform: rotate(-8deg); line-height: 1.3; }

  .footer {
    position: absolute; left: 0; bottom: 0; width: 100%; height: 27px;
    background: var(--footer); color: #fff; font-size: 9px;
    display: flex; align-items: center; justify-content: center; letter-spacing: .2px;
  }

  /* brand name, set as plain text */
  .brand-name { position: absolute; font-weight: 700; color: var(--ink-soft); }
  .brand-name--front { left: 300px; top: 100px; width: 200px; text-align: center;
    font-size: 11px; color: var(--orange); }
  .brand-name--back { left: 26px; top: 16px; font-size: 12.5px; line-height: 16px;
    display: flex; align-items: center; gap: 8px; }
  .brand-dot { width: 12px; height: 12px; border-radius: 50%; background: var(--orange); flex: none; }

  /* front page */
  .title { position: absolute; left: 300px; top: 140px; width: 200px; text-align: center;
    font-weight: 800; font-size: 24px; line-height: 25px; }
  .title .dark { color: var(--ink); }
  .title .accent { color: var(--orange); }
  .intro { position: absolute; left: 20px; top: 394px; width: 473px; text-align: center;
    font-size: 12.4px; line-height: 17.4px; color: var(--ink-soft); }
  .intro b { color: var(--ink); font-weight: 800; }
  .benefit-box { position: absolute; left: 24px; top: 468px; width: 205px; height: 200px;
    background: var(--panel); border-radius: 4px; box-shadow: 0 2px 4px rgba(0,0,0,.15);
    font-size: 8.6px; line-height: 12.5px; padding: 15px 11px; }
  .benefit { position: absolute; left: 9px; display: flex; align-items: center; gap: 8px;
    font-weight: 800; }
  .benefit .num { width: 20px; height: 20px; border-radius: 50%; background: var(--orange);
    color: #fff; font-size: 10px; display: flex; align-items: center; justify-content: center; flex: none; }
  .body-copy { position: absolute; left: 248px; top: 467px; width: 250px;
    font-size: 8.6px; line-height: 12.9px; }
  .body-copy strong { display: block; margin-top: 13px; font-weight: 800; color: #1f1f20; }

  /* back page */
  .section-title { position: absolute; left: 30px; top: 162px; font-size: 13.5px; font-weight: 800; }
  .col { position: absolute; font-size: 8.6px; line-height: 12.9px; }
  .col h3 { color: var(--orange); font-size: 11px; font-weight: 800; margin-bottom: 3px; }
  .col p { margin-bottom: 2px; }
  .checks { list-style: none; }
  .checks li { position: relative; padding-left: 11px; margin-bottom: 2.4px; }
  .checks li::before { content: "✓"; position: absolute; left: 0; top: 0; font-weight: 700; }
  .gap { margin-top: 12px; }

  .cost-box { position: absolute; left: 19px; top: 535px; width: 310px; height: 147px;
    background: var(--panel); border-radius: 4px; box-shadow: 0 2px 4px rgba(0,0,0,.15);
    padding: 9px 12px; font-size: 8.6px; line-height: 12.9px; }
  .cost-box h3 { font-size: 13px; font-weight: 800; margin-bottom: 5px; }
  .cost-box p { margin-bottom: 1.5px; }

  .contact-photo { position: absolute; left: 354px; top: 515px; width: 50px; height: 60px;
    border-radius: 3px; background: linear-gradient(180deg, #d9d6d2, #b7c4a6); }
  .contact-label { position: absolute; left: 413px; top: 532px; font-size: 8.8px;
    line-height: 10.5px; font-weight: 800; }
  .company-name { position: absolute; left: 354px; top: 586px; width: 150px; font-size: 12px;
    line-height: 14px; font-weight: 800; color: var(--orange); }
  .address { position: absolute; left: 354px; top: 626px; font-size: 8.6px; line-height: 10.3px;
    color: var(--ink-soft); }
  .address b { color: var(--ink); font-weight: 800; }
</style>
</head>
<body>

<!-- Front page -->
<section class="page page--front">
  <svg class="hero" width="513" height="380" viewBox="0 0 513 380">
    <defs>
      <linearGradient id="front-photo" x1="0" y1="0" x2="1" y2="0.4">
        <stop offset="0" stop-color="#b9bcc0"/>
        <stop offset="0.35" stop-color="#7d736c"/>
        <stop offset="0.55" stop-color="#c7d0d4"/>
        <stop offset="1" stop-color="#eef2f3"/>
      </linearGradient>
    </defs>
    <path d="M0 0 H513 V300 C380 345 200 365 0 352 Z" fill="url(#front-photo)"
          role="img" aria-label="Foto: zwei Kolleginnen geben sich fröhlich ein High Five im Büro"/>
    <path d="M0 352 C200 365 380 345 513 300 V312 C380 360 200 378 0 366 Z" fill="var(--band)"/>
  </svg>

  <div class="brand-name brand-name--front">Praxisverbund Lindenhof</div>

  <h1 class="title">
    <span class="dark">Betriebliche</span><br>
    <span class="accent">Gesundheits-<br>förderung</span>
  </h1>

  <div class="badge" style="left:402px; top:283px; width:80px; height:80px; font-size:8.6px;">
    <span>Jetzt einen<br>persönlichen<br>Termin<br>vereinbaren!</span>
  </div>

  <p class="intro">
    Die betriebliche Gesundheitsförderung hat das Ziel die<br>
    <b>Gesundheit der Mitarbeiter</b> zu erhalten und zu fördern sowie die<br>
    <b>Leistungsfähigkeit und Motivation</b> der Belegschaft zu steigern.
  </p>

  <div class="benefit-box">
    <p>Immer mehr gewinnen jedoch<br>folgende Punkte an Bedeutung für<br>Unternehmen:</p>
    <div class="benefit" style="top:62px;"><span class="num">1.</span><span>Mitarbeiterbindung &amp;</span></div>
    <div class="benefit" style="top:98px;"><span class="num">2.</span><span>Arbeitgeber Attraktivität zu<br>erhöhen, um ein Vorteil am<br>Bewerbermarkt zu erzielen.</span></div>
    <p style="position:absolute; left:11px; top:153px;">Auch da können wir Sie mit unserem<br>Know-How und abgerundeten Konzept<br>unterstützen.</p>
  </div>

  <div class="body-copy">
    <p>In regelmäßigen Abständen setzen wir uns mit Ihren<br>
    Mitarbeitern in Verbindung und erfragen den jeweiligen<br>
    IST Stand und besprechen gemeinsames Vorgehen,<br>
    um gesundheitliche Problematiken im Handlungsfeld<br>
    Bewegung und Entspannung präventiv vorzubeugen.<br>
    Ihre Mitarbeiter werden dadurch in festen monatlichen<br>
    Intervallen sensibilisiert dass Sie sich um das<br>
    Wohlbefinden Ihrer Mitarbeiter kümmern und Sie<br>
    auch darin investieren.</p>
    <strong>Sie als Arbeitgeber können nicht wissen und auch<br>
    zeitlich nicht gewährleisten welche individuellen<br>
    gesundheitlichen Problematiken Ihre Mitarbeiter<br>
    haben. Deshalb bieten wir Ihnen eine individuelle<br>
    Lösung an Dienstleistung, welche den individuellen<br>
    Bedarf Ihrer Mitarbeiter deckt.</strong>
  </div>

  <footer class="footer">www.therapie-lindenhof.de</footer>
</section>

<!-- Back page -->
<section class="page page--back">
  <svg class="hero" width="513" height="190" viewBox="0 0 513 190">
    <defs>
      <linearGradient id="back-photo" x1="0" y1="0" x2="1" y2="0">
        <stop offset="0" stop-color="#e4e4e4"/>
        <stop offset="0.5" stop-color="#d2d2d2"/>
        <stop offset="0.72" stop-color="#e3a68a"/>
        <stop offset="1" stop-color="#ecdcd4"/>
      </linearGradient>
    </defs>
    <path d="M0 0 H513 V150 C420 170 320 152 220 146 C130 141 60 146 0 152 Z" fill="url(#back-photo)"
          role="img" aria-label="Foto: Therapeutin im Trainingsraum mit Laptop, der eine Körperanalyse zeigt"/>
    <path d="M0 152 C60 146 130 141 220 146 C320 152 420 170 513 150 V160 C420 180 320 160 220 154 C130 149 60 154 0 160 Z" fill="var(--band)"/>
  </svg>

  <div class="brand-name brand-name--back"><span class="brand-dot"></span><span>Praxisverbund<br>Lindenhof</span></div>

  <div class="badge" style="left:359px; top:80px; width:84px; height:84px; font-size:8.6px;">
    <span>Jetzt einen<br>persönlichen<br>Termin<br>vereinbaren!</span>
  </div>

  <h2 class="section-title">Unsere Leistungen</h2>

  <div class="col" style="left:30px; top:194px; width:230px;">
    <h3>Messung &amp; Analysen</h3>
    <ul class="checks">
      <li>Messung &amp; Analysen zur individuellen Stress-<br>und Resilienzdiagnostik um zielorientiert ein<br>Stressmanagment in Ihrem Betrieb zu<br>implementieren.</li>
      <li>Dokumentation von Körperdaten und Risiko-<br>faktoren in einer Eingangskontrolle und einem<br>½ jährlichen Wiederholung der Kontrolle.</li>
      <li>Wirbelsäulen- und Haltungsscreenings, Haltung,<br>Beweglichkeit und Haltungskomponenten<br>werden anschaulich dargestellt und bilden die<br>Basis für zielführende Visualisierung und<br>fundierte Übungsempfehlung.</li>
      <li>Analysen von Körperstabilität und Gleichgewicht;<br>Balance Scan Pro ist ein erprobtes Analysetool für<br>das Thema Körperstabilität</li>
    </ul>
    <h3 class="gap">Mentale Gesundheit</h3>
    <p>Programme zur Achtsamkeit, Entspannung,<br>und Wahrnehmung. In Kleingruppen, Online</p>
    <h3 class="gap">Gesundheitstage für Firmen</h3>
    <p>Individuell auf Ihre Firma abgestimmt.</p>
  </div>

  <div class="col" style="left:284px; top:194px; width:215px;">
    <h3>Bewegungsprogramme:</h3>
    <p style="margin-bottom:4px;">Präventionsprogramme nach §20 zertifiziert<br>von den Krankenkassen wie zum Beispiel:</p>
    <ul class="checks">
      <li>Entspannungskurse Hatha Yoga</li>
      <li>Pilates</li>
      <li>Rückengymnastik</li>
      <li>Ganzkörper Training an Geräten</li>
      <li>Fit am Arbeitsplatz</li>
      <li>Online-Präventionskurs<br>(zeitlich und räumlich unabhängig)</li>
      <li>und einige mehr....</li>
    </ul>
    <h3 class="gap">Digitaler Gesundheitscoach</h3>
    <ul class="checks">
      <li>Workouts</li>
      <li>Live Online- Kurse</li>
      <li>Physio Übungen gezielt und individuell<br>in der Einzelberatung online und persönlich<br>abgestimmt</li>
      <li>Online Präventionscoach<br>oder als Einzelleistung buchbar</li>
      <li>Online Präventionscoach</li>
    </ul>
  </div>

  <div class="cost-box">
    <h3>Informationen zu den Kosten</h3>
    <p>Bis zu 600 € können Sie, als Arbeitgeber steuerfrei bezuschussen.<br>
    Voraussetzung dafür ist, dass die fachlichen Anforderungen des<br>
    Kassen-Dachverbandes erfüllt werden.</p>
    <p>Diese Leistungen können wir erfüllen und einige mehr on Top.<br>
    Lassen Sie sich persönlich und individuell beraten und nehmen<br>
    Sie persönlich oder via E-Mail Kontakt mit uns auf.</p>
    <p>Senden Sie uns eine E-Mail an albers@therapie-lindenhof.de<br>
    und wir melden uns umgehend für eine kostenlose Beratung.</p>
  </div>

  <div class="contact-photo" role="img" aria-label="Porträtfoto der Ansprechpartnerin"></div>
  <p class="contact-label">Ihre<br>Ansprechpartnerin<br>Katrin Albers</p>

  <div class="company-name">Therapiezentrum<br>Lindenhof</div>

  <p class="address">
    <b>Therapiezentrum Lindenhof</b><br>
    Ahornweg 14<br>
    46100 Musterstadt<br>
    <span style="display:block; margin-top:4px;">01234 - 56 78 90<br>albers@therapie-lindenhof.de</span>
  </p>

  <footer class="footer">www.therapie-lindenhof.de</footer>
</section>

</body>
</html>
```